Bref créative
Sign for Retail Store
The Velvet Fern Parlour
We need a sign for our retail/service business. Please see attached photos for size.
Retailers
Women over 30, some men.
Our existing logo and colors, which will be uploaded as well.
Logo file .AI

```html
<!DOCTYPE html>
<html lang="en">
<head>
<meta charset="utf-8">
<title>The Velvet Fern Parlour – Storefront Sign</title>
<link href="https://fonts.googleapis.com/css2?family=Questrial&display=swap" rel="stylesheet">
<style>
  :root {
    --backdrop: #a7a7a7;
    --post-fill: #ffffff;
    --post-line: #2b2b2b;
    --band: #000000;
    --panel-light: #f4f4f4;
    --panel-mid: #d9d9d9;
    --panel-dark: #a9a9a9;
    --brand-green: #8dc63f;
    --ink: #3a3a3a;
  }
  html, body {
    margin: 0;
    padding: 0;
    overflow: hidden;
  }
  body {
    width: 1200px;
    height: 857px;
    background: var(--backdrop);
  }
  .sign {
    display: block;
    width: 1200px;
    height: 857px;
  }
  .post-body, .post-cap, .post-collar {
    fill: var(--post-fill);
    stroke: var(--post-line);
    stroke-width: 2.5;
  }
  .sign-band { fill: var(--band); }
  .brand-mark { fill: var(--brand-green); }
  .brand-name {
    font-family: "Questrial", sans-serif;
    fill: var(--ink);
    letter-spacing: -1px;
  }
</style>
</head>
<body>
<svg class="sign" viewBox="0 0 1200 857" xmlns="http://www.w3.org/2000/svg">
  <defs>
    <radialGradient id="panel-tone" cx="0.45" cy="0.45" r="0.75">
      <stop offset="0" stop-color="var(--panel-light)"/>
      <stop offset="0.55" stop-color="var(--panel-mid)"/>
      <stop offset="1" stop-color="var(--panel-dark)"/>
    </radialGradient>
  </defs>

  <!-- left post -->
  <g class="post post-left">
    <rect class="post-body" x="120" y="150" width="67" height="680"/>
    <rect class="post-collar" x="114" y="124" width="79" height="26"/>
    <path class="post-cap" d="M120 124 L120 96 Q120 62 153.5 43 Q187 62 187 96 L187 124 Z"/>
  </g>

  <!-- right post -->
  <g class="post post-right">
    <rect class="post-body" x="1018" y="150" width="67" height="680"/>
    <rect class="post-collar" x="1012" y="124" width="79" height="26"/>
    <path class="post-cap" d="M1018 124 L1018 96 Q1018 62 1051.5 43 Q1085 62 1085 96 L1085 124 Z"/>
  </g>

  <!-- sign board -->
  <g class="sign-board">
    <rect class="sign-band sign-band-top" x="187" y="156" width="831" height="26"/>
    <rect class="sign-panel" x="187" y="182" width="831" height="327" fill="url(#panel-tone)"
          role="img" aria-label="Soft grey botanical leaf pattern background"/>
    <rect class="sign-band sign-band-bottom" x="187" y="509" width="831" height="24"/>
  </g>

  <!-- brand -->
  <g class="brand">
    <circle class="brand-mark" cx="355" cy="336" r="70"/>
    <text class="brand-name" x="490" y="280" font-size="82">the</text>
    <text class="brand-name" x="490" y="370" font-size="82">velvet fern</text>
    <text class="brand-name" x="490" y="456" font-size="82">parlour</text>
  </g>
</svg>
</body>
</html>
```